Creating the Look and Feel of an Elite Boutique Consulting Practice: Vane Advisory

Complete a professional website on Weebly. As part of the site, we are open to a new logo -- we have just launched. We put up a starter website that shows you the content and theme we are going for. But clearly we aren't professional web designers and we need your help. Check out our start at vaneadvisory.com

Target Market(s)

Fortune 500 Clients

Industry/Entity Type

Management Consulting

Logo Text

VANE Advisory

Number of Pages Required

4 page

Requirements
Must have
• I've already set us up on Weebly. I'd like to give the selected designer the log-in credentials and have the designer create it on Weebly, so we can maintain it through that service.

```html
<!DOCTYPE html>
<html lang="en">
<head>
<meta charset="utf-8">
<title>Vane Advisory</title>
<link rel="stylesheet" href="https://fonts.googleapis.com/css2?family=Open+Sans:wght@300;400;600;700;800&display=swap">
<style>
  :root {
    --white: #ffffff;
    --ink-dark: #201e1f;
    --muted: #9a9899;
    --footer-bg: #ffffff;
    --footer-text: #555555;
    --hero-top: #5d5343;
    --hero-mid: #7a6a4e;
    --hero-low: #6b6845;
  }
  * { margin: 0; padding: 0; box-sizing: border-box; }
  html, body { width: 1200px; height: 1098px; overflow: hidden; }
  body { font-family: "Open Sans", sans-serif; color: var(--white); background: var(--footer-bg); }

  .hero { position: relative; width: 1200px; height: 658px; overflow: hidden; }
  .hero-backdrop {
    position: absolute; inset: 0;
    background:
      radial-gradient(ellipse at 55% 60%, rgba(190,160,110,.45), transparent 60%),
      linear-gradient(180deg, var(--hero-top) 0%, #6e604a 30%, var(--hero-mid) 60%, var(--hero-low) 100%);
  }
  .brand { position: absolute; left: 98px; top: 72px; display: flex; align-items: center; gap: 10px; }
  .brand-mark { width: 14px; height: 14px; border-radius: 50%; background: var(--white); }
  .brand-name { font-size: 27px; font-weight: 400; letter-spacing: .5px; color: var(--white); text-transform: uppercase; }

  .main-nav { position: absolute; top: 58px; left: 0; width: 100%; }
  .main-nav a {
    position: absolute; font-size: 13.5px; font-weight: 700; color: var(--white);
    text-decoration: none; letter-spacing: .2px;
  }
  .menu-toggle { position: absolute; left: 1080px; top: 55px; width: 22px; }
  .menu-toggle span { display: block; height: 3px; background: var(--white); margin-bottom: 6px; }

  .slide-dots { position: absolute; left: 1092px; top: 255px; }
  .slide-dots span { display: block; width: 8px; height: 8px; border-radius: 50%; background: var(--white); margin-bottom: 17px; }
  .slide-dots span.current { background: transparent; border: 1.5px solid var(--white); }

  .hero-copy { position: absolute; top: 290px; left: 0; width: 100%; text-align: center; }
  .hero-question { font-size: 23px; font-weight: 300; letter-spacing: 5.4px; }
  .hero-claim { font-size: 31px; font-weight: 800; margin-top: 10px; letter-spacing: .2px; }

  .strengths { position: relative; height: 346px; background: var(--ink-dark); }
  .strengths h2 { position: absolute; top: 53px; width: 100%; text-align: center; font-size: 27px; font-weight: 800; letter-spacing: .3px; }
  .strengths .lead { position: absolute; top: 100px; width: 100%; text-align: center; font-size: 17px; font-weight: 400; }
  .feature { position: absolute; top: 166px; width: 300px; }
  .feature-icon {
    position: absolute; left: 0; top: 0; width: 52px; height: 52px; border-radius: 50%;
    border: 1px solid var(--white); display: flex; align-items: center; justify-content: center;
  }
  .feature h3 { position: absolute; left: 72px; top: 4px; font-size: 13px; font-weight: 700; white-space: nowrap; }
  .feature p { position: absolute; left: 72px; top: 31px; width: 236px; font-size: 11.2px; line-height: 20.6px; color: var(--muted); }
  .carousel-arrow { position: absolute; top: 208px; }

  .site-footer { position: relative; height: 94px; background: var(--footer-bg); color: var(--footer-text); }
  .legal { position: absolute; left: 101px; top: 41px; font-size: 9.5px; letter-spacing: 1.9px; text-transform: uppercase; }
  .legal .sep { margin: 0 10px; }
  .follow { position: absolute; left: 861px; top: 41px; font-size: 9.5px; letter-spacing: 1.9px; text-transform: uppercase; display: flex; align-items: center; }
  .follow .social { display: inline-block; width: 10px; height: 10px; border-radius: 50%; background: #777; margin-left: 24px; }
  .follow .social:first-of-type { margin-left: 16px; }
</style>
</head>
<body>
  <header class="hero">
    <div class="hero-backdrop" role="img" aria-label="Aerial photograph of a dense city skyline with skyscrapers beside a river, warm sepia tones"></div>
    <div class="brand"><span class="brand-mark"></span><span class="brand-name">Vane Advisory</span></div>
    <nav class="main-nav">
      <a href="#" style="left:611px">ABOUT VANE</a>
      <a href="#" style="left:752px">APPROACH</a>
      <a href="#" style="left:884px">TEAM</a>
      <a href="#" style="left:980px">CONTACT</a>
    </nav>
    <div class="menu-toggle"><span></span><span></span><span></span></div>
    <div class="slide-dots"><span class="current"></span><span></span><span></span><span></span><span></span></div>
    <div class="hero-copy">
      <p class="hero-question">DO YOU NEED TO TRANSFORM YOUR ORGANIZATION?</p>
      <h1 class="hero-claim">LET'S CHART YOUR PATH TO SUCCESS</h1>
    </div>
  </header>

  <section class="strengths">
    <h2>WE HELP YOUR ORGANIZATION</h2>
    <p class="lead">THE PEOPLE OF VANE ADVISORY&nbsp; ARE</p>

    <svg class="carousel-arrow" style="left:49px" width="14" height="40" viewBox="0 0 14 40"><path d="M13 0 L1 20 L13 40" fill="none" stroke="#444" stroke-width="1.2"/></svg>
    <svg class="carousel-arrow" style="left:1137px" width="14" height="40" viewBox="0 0 14 40"><path d="M1 0 L13 20 L1 40" fill="none" stroke="#444" stroke-width="1.2"/></svg>

    <div class="feature" style="left:99px">
      <div class="feature-icon">
        <svg width="24" height="22" viewBox="0 0 24 22"><circle cx="8" cy="12" r="5" fill="none" stroke="#fff" stroke-width="3" stroke-dasharray="2.5 1.4"/><circle cx="8" cy="12" r="1.6" fill="#fff"/><circle cx="18" cy="6" r="3.5" fill="none" stroke="#fff" stroke-width="2.4" stroke-dasharray="2 1.2"/><circle cx="18" cy="16" r="3" fill="none" stroke="#fff" stroke-width="2.2" stroke-dasharray="2 1.2"/></svg>
      </div>
      <h3>EXPERIENCED</h3>
      <p>Over the past three decades, we have deep experience driving organizational transformation in more than 33 countries, for some...</p>
    </div>
    <div class="feature" style="left:446px">
      <div class="feature-icon">
        <svg width="22" height="24" viewBox="0 0 22 24"><circle cx="11" cy="6" r="5" fill="#fff"/><path d="M1 23 Q1 13 11 13 Q21 13 21 23 Z" fill="#fff"/><path d="M11 14 L9.5 20 L11 22 L12.5 20 Z" fill="#201e1f"/></svg>
      </div>
      <h3>CURIOUS</h3>
      <p>Over the past three decades, we have deep experience driving organizational transformation in more than 33 countries, for some...</p>
    </div>
    <div class="feature" style="left:794px">
      <div class="feature-icon">
        <svg width="20" height="24" viewBox="0 0 20 24"><path d="M2 1 H13 L18 6 V23 H2 Z" fill="none" stroke="#fff" stroke-width="1.8"/><path d="M6 11 H14 M6 14.5 H14 M6 18 H14" stroke="#fff" stroke-width="1.6"/></svg>
      </div>
      <h3>READY TO HEAR YOUR STORY</h3>
      <p>Over the past three decades, we have deep experience driving organizational transformation in more than 33 countries, for some...</p>
    </div>
  </section>

  <footer class="site-footer">
    <p class="legal">© 2015. Vane Advisory. All rights reserved.<span class="sep">/</span> Terms &amp; Conditions <span class="sep">/</span> Privacy Policy</p>
    <div class="follow">Follow us :<span class="social"></span><span class="social"></span><span class="social"></span><span class="social"></span><span class="social"></span></div>
  </footer>
</body>
</html>
```